Mezzanine Floor Manufacturer looking for a new business card design

We manufacture mezzanine floors and are providers of racking systems. We provide a range of items/services - simple rack repairs , full warehouse fit outs , manufacturer and install mezzanine floors , partitioning and large turnkey projects. Recently had a new website - www.corrowden-racking.co.uk and would like our business cards updating aswell . Our current card is single sided in the old logo colours (pdf attached) and needs updating.

Target Market(s)

We deal with large projects/ multi national companies and also smaller projects and companies throughout the UK ranging from a single warehouse to a large multi site company.

Industry/Entity Type

Business

Contact Information for Business Card

Will have job title,tel no's, email ,website address etc like example pdf

Requirements
Must have
• Hi - needs to use the colours of the logo & new website. Card needs to be professional

```html
<!DOCTYPE html>
<html lang="en">
<head>
<meta charset="utf-8">
<title>Corrowden Racking – Business Card</title>
<link href="https://fonts.googleapis.com/css2?family=Lato:wght@400;700;900&display=swap" rel="stylesheet">
<style>
  :root {
    --brand-red: #dc2b1c;
    --ink: #1b1b1b;
    --paper: #ffffff;
    --backdrop: #e4e4e4;
    --rule: #2a2a2a;
  }
  * { box-sizing: border-box; margin: 0; padding: 0; }
  html, body {
    width: 1200px; height: 675px; overflow: hidden;
    background: var(--backdrop);
    font-family: "Lato", sans-serif;
  }
  .canvas {
    width: 1200px; height: 675px;
    display: flex; align-items: center; justify-content: center; gap: 60px;
  }
  .card {
    width: 520px; height: 297px; position: relative; overflow: hidden;
    box-shadow: 0 6px 18px rgba(0,0,0,0.15);
  }

  /* Front */
  .card-front { background: var(--brand-red); color: var(--paper); }
  .front-mark {
    position: absolute; left: 0; right: 0; top: 100px;
    display: flex; align-items: center; justify-content: center; gap: 14px;
  }
  .mark-dot { width: 34px; height: 34px; border-radius: 50%; background: var(--paper); }
  .front-mark .mark-name { font-weight: 900; font-size: 46px; letter-spacing: 1px; color: var(--paper); }
  .front-url {
    position: absolute; left: 0; right: 0; top: 210px; text-align: center;
    font-size: 15px; letter-spacing: 3px;
  }

  /* Back */
  .card-back { background: var(--paper); color: var(--ink); }
  .back-mark {
    position: absolute; left: 52px; top: 92px;
    display: flex; align-items: center; gap: 10px;
  }
  .back-mark .mark-dot { background: var(--brand-red); width: 26px; height: 26px; }
  .back-mark .mark-name { font-weight: 900; font-size: 36px; color: var(--brand-red); }
  .holder { position: absolute; right: 34px; top: 54px; text-align: right; }
  .holder-name { font-size: 21px; }
  .holder-role { font-size: 14px; color: var(--brand-red); margin-top: 1px; }
  .divider {
    position: absolute; left: 34px; right: 34px; top: 170px;
    height: 1px; background: var(--rule);
  }
  .contacts { position: absolute; left: 38px; top: 182px; list-style: none; }
  .contacts li {
    display: flex; align-items: center; gap: 9px;
    font-size: 14px; line-height: 20px;
  }
  .contacts svg { width: 13px; height: 13px; fill: var(--brand-red); flex: none; }
  .address {
    position: absolute; right: 34px; top: 182px; text-align: right;
    font-size: 13.5px; line-height: 18px; font-style: normal;
  }
  .base-band {
    position: absolute; left: 0; right: 0; bottom: 0; height: 16px; background: var(--ink);
  }
  .url-tab {
    position: absolute; right: 0; bottom: 0; width: 232px; height: 38px;
    background: var(--brand-red); border-top-left-radius: 22px;
    color: var(--paper); font-size: 14px;
    display: flex; align-items: center; justify-content: center;
  }
</style>
</head>
<body>
<main class="canvas">
  <section class="card card-front" aria-label="Card front">
    <div class="front-mark">
      <span class="mark-dot"></span>
      <span class="mark-name">Corrowden</span>
    </div>
    <p class="front-url">www.corrowden-racking.co.uk</p>
  </section>

  <section class="card card-back" aria-label="Card back">
    <div class="back-mark">
      <span class="mark-dot"></span>
      <span class="mark-name">Corrowden</span>
    </div>
    <div class="holder">
      <p class="holder-name">Daniel Whitmore</p>
      <p class="holder-role">Technical sales</p>
    </div>
    <div class="divider"></div>
    <ul class="contacts">
      <li><svg viewBox="0 0 24 24"><path d="M6.6 10.8a15.1 15.1 0 0 0 6.6 6.6l2.2-2.2c.3-.3.7-.4 1-.2 1.1.4 2.3.6 3.6.6.6 0 1 .4 1 1V20c0 .6-.4 1-1 1A17 17 0 0 1 3 4c0-.6.4-1 1-1h3.5c.6 0 1 .4 1 1 0 1.3.2 2.5.6 3.6.1.3 0 .7-.2 1z"/></svg>01632 960418</li>
      <li><svg viewBox="0 0 24 24"><path d="M7 1h10a2 2 0 0 1 2 2v18a2 2 0 0 1-2 2H7a2 2 0 0 1-2-2V3a2 2 0 0 1 2-2zm0 3v14h10V4zm5 15.5a1.2 1.2 0 1 0 0 2.4 1.2 1.2 0 0 0 0-2.4z"/></svg>07700 900327</li>
      <li><svg viewBox="0 0 24 24"><path d="M6 2h9l3 3v4H6zm-3 8h18a1 1 0 0 1 1 1v8a1 1 0 0 1-1 1h-3v2H6v-2H3a1 1 0 0 1-1-1v-8a1 1 0 0 1 1-1zm5 7v3h8v-3z"/></svg>01632 960592</li>
      <li><svg viewBox="0 0 24 24"><path d="M2 5h20v14H2zm2 2v.5l8 5.5 8-5.5V7zm0 2.9V17h16V9.9l-8 5.5z"/></svg>info@corrowden-racking.co.uk</li>
    </ul>
    <address class="address">
      Twelve Mill Lane<br>
      Ashcombe Trade Park<br>
      Belper, Derbyshire DE56 4TR
    </address>
    <div class="base-band"></div>
    <div class="url-tab">www.corrowden-racking.co.uk</div>
  </section>
</main>
</body>
</html>
```